Poster for mountain bike and trail run competition

I am looking for a poster design for a charitable mountain bike and trail run race. It should be something fun, colorful, which can attract participants. The area in which the competition takes place is dominated by hills and by the Nera river which has a beautiful gorge.. I am attaching some of our previous (poorly designed) posters. The poster should have a place where I can add the sponsor logos, which I will do by myself, in the following months.
Text:
Headline: "Valea Murgului Mountain Bike and Trail Run Race"
small headline: "Editia a-6a"
small headline: "Lunca Verde, 10-11 IUNIE 2023"
other text:
"10 IUNIE - Concurs Mountain Bike & Concert
11 IUNIE - Concurs Trail Run"
text for enrollments: "inscrieri pe www.tornaluride.ro"

Thanks

• a space where I can add sponsor logos, editable file to be provided (AI, photoshop or corel)

```html
<!DOCTYPE html>
<html lang="ro">
<head>
<meta charset="utf-8">
<title>Valea Murgului Mountain Bike &amp; Trail Run Race</title>
<link rel="stylesheet" href="https://fonts.googleapis.com/css2?family=Titan+One&family=Fredoka:wght@600;700&family=Poppins:wght@400;700&display=swap">
<style>
  :root{
    --page:#ececee;
    --ink-dark:#231f2c;
    --plum:#453a66;
    --plum-soft:#6d6290;
    --band:#463a68;
    --sky-top:#ecdcf0;
    --sky-pink:#f6d9ee;
    --sky-mid:#ddd0ea;
    --mist:#c9c3e4;
    --hill-light:#a99bc8;
    --hill-mid:#76699a;
    --hill-deep:#5a4d82;
    --white:#ffffff;
  }
  *{margin:0;padding:0;box-sizing:border-box}
  html,body{width:1200px;height:2284px;overflow:hidden;background:var(--page)}
  .poster{position:absolute;left:0;top:294px;width:1200px;height:1697px;background:var(--white);overflow:hidden;box-shadow:0 20px 50px rgba(0,0,0,.18)}
  .scene{position:absolute;left:0;top:0;width:1200px;height:1218px;
    background:
      radial-gradient(ellipse 520px 120px at 260px 90px, rgba(246,205,236,.9), rgba(246,205,236,0)),
      radial-gradient(ellipse 420px 90px at 1120px 250px, rgba(248,214,238,.85), rgba(248,214,238,0)),
      radial-gradient(ellipse 600px 70px at 330px 390px, rgba(255,255,255,.75), rgba(255,255,255,0)),
      radial-gradient(ellipse 520px 140px at 880px 760px, rgba(196,190,228,.9), rgba(196,190,228,0)),
      radial-gradient(ellipse 700px 260px at 1180px 900px, rgba(70,58,104,.55), rgba(70,58,104,0)),
      linear-gradient(160deg, rgba(0,0,0,0) 52%, rgba(94,80,136,.55) 64%, rgba(70,58,104,.0) 80%),
      linear-gradient(180deg,var(--sky-top) 0%,var(--sky-mid) 34%,#d6c8e6 50%,var(--mist) 58%,var(--hill-light) 66%,var(--hill-mid) 76%,var(--hill-deep) 88%,var(--band) 100%)}
  .title{position:absolute;left:0;width:100%;text-align:center;font-family:"Titan One",sans-serif;line-height:1;letter-spacing:2px;text-shadow:-5px 4px 0 rgba(255,255,255,.85)}
  .title--first{top:52px;font-size:185px;color:var(--plum)}
  .title--second{top:226px;font-size:178px;color:var(--plum-soft);transform:scaleX(.8);letter-spacing:0}
  .subtitle{position:absolute;left:0;width:100%;text-align:center;font-family:"Titan One",sans-serif;color:var(--ink-dark);font-size:80px;line-height:1}
  .subtitle--bike{top:424px}
  .subtitle--run{top:502px}
  .rule{position:absolute;height:3px;background:var(--plum)}
  .rule--head{left:214px;width:776px;top:613px}
  .edition{position:absolute;left:0;width:100%;top:628px;text-align:center;font-family:"Fredoka",sans-serif;font-weight:700;font-size:62px;color:var(--plum);line-height:1}
  .edition::before,.edition::after{content:"";display:inline-block;width:24px;height:3px;background:var(--plum);vertical-align:middle;margin:0 10px}
  .band{position:absolute;left:0;top:1217px;width:1200px;height:300px;background:var(--band)}
  .info{position:absolute;font-family:"Fredoka",sans-serif;font-weight:700;color:var(--white);line-height:1}
  .icon{position:absolute}
  .place{left:198px;top:1228px;font-size:60px}
  .dates{left:868px;top:1228px;font-size:60px}
  .dates small{position:absolute;left:160px;top:4px;font-size:25px;line-height:.95}
  .rule--light{background:rgba(255,255,255,.55);height:2px}
  .day{top:1312px;font-size:64px}
  .day--one{left:106px}
  .day--two{left:718px}
  .day-note{position:absolute;top:1318px;font-family:"Poppins",sans-serif;font-size:24px;line-height:1.02;color:var(--white)}
  .day-note--one{left:380px}
  .day-note--two{left:973px}
  .divider{position:absolute;left:666px;top:1306px;width:2px;height:66px;background:rgba(255,255,255,.55)}
  .signup{position:absolute;left:195px;top:1403px;width:812px;height:52px;border:3px solid var(--white);border-radius:26px;display:flex;overflow:hidden}
  .signup__label{width:308px;background:var(--white);color:var(--band);font-family:"Fredoka",sans-serif;font-weight:700;font-size:38px;display:flex;align-items:center;justify-content:center;border-radius:0 26px 26px 0}
  .signup__url{flex:1;color:var(--white);font-family:"Poppins",sans-serif;font-weight:700;font-size:30px;letter-spacing:7px;display:flex;align-items:center;justify-content:center}
  .sponsor-label{position:absolute;left:0;width:100%;top:1476px;text-align:center;font-family:"Poppins",sans-serif;font-weight:700;font-size:14px;color:var(--white)}
  .sponsor-area{position:absolute;left:0;top:1517px;width:1200px;height:166px;background:var(--white)}
  .foot-stripe{position:absolute;left:0;top:1683px;width:1200px;height:14px;background:var(--band)}
</style>
</head>
<body>
  <main class="poster">
    <div class="scene" role="img" aria-label="Illustration of misty purple hills with trees, two trail runners and a mountain biker"></div>

    <h1 class="title title--first">VALEA</h1>
    <div class="title title--second">MURGULUI</div>
    <div class="subtitle subtitle--bike">MOUNTAIN BIKE</div>
    <div class="subtitle subtitle--run">&amp; TRAIL RUN RACE</div>
    <div class="rule rule--head"></div>
    <div class="edition">EDITIA A-6A</div>

    <div class="band"></div>

    <svg class="icon" style="left:116px;top:1232px" width="50" height="50" viewBox="0 0 50 50" aria-hidden="true">
      <circle cx="25" cy="25" r="24" fill="#fff"/>
      <path d="M25 11c-6 0-10 4.5-10 10 0 7 10 17 10 17s10-10 10-17c0-5.5-4-10-10-10z" fill="var(--band)"/>
      <circle cx="25" cy="21" r="4" fill="#fff"/>
    </svg>
    <div class="info place">LUNCA VERDE</div>

    <svg class="icon" style="left:790px;top:1232px" width="50" height="50" viewBox="0 0 50 50" aria-hidden="true">
      <circle cx="25" cy="25" r="24" fill="#fff"/>
      <rect x="13" y="15" width="24" height="21" rx="3" fill="var(--band)"/>
      <rect x="16" y="21" width="18" height="12" fill="#fff"/>
      <g fill="var(--band)"><rect x="18" y="23" width="3" height="3"/><rect x="23.5" y="23" width="3" height="3"/><rect x="29" y="23" width="3" height="3"/><rect x="18" y="28" width="3" height="3"/><rect x="23.5" y="28" width="3" height="3"/><rect x="29" y="28" width="3" height="3"/></g>
    </svg>
    <div class="info dates">10-11<small>IUNIE<br>2023</small></div>

    <div class="rule rule--light" style="left:111px;width:978px;top:1296px"></div>
    <div class="info day day--one">10 IUNIE</div>
    <div class="day-note day-note--one">Concurs Mountain<br>Bike &amp; Concert</div>
    <div class="divider"></div>
    <div class="info day day--two">11 IUNIE</div>
    <div class="day-note day-note--two">Concurs<br>Trail Run</div>
    <div class="rule rule--light" style="left:111px;width:978px;top:1378px"></div>

    <div class="signup">
      <span class="signup__label">inscrieri pe</span>
      <span class="signup__url">www.tornaluride.ro</span>
    </div>
    <div class="sponsor-label">SPONSOR PRINCIPAL</div>

    <div class="sponsor-area"></div>
    <div class="foot-stripe"></div>
  </main>
</body>
</html>
```